Fin-Tech Firm Captivating Business Card Design

We need a logo design as well to compliment this business card.

We are a new startup based in Singapore called 'Quorvane Systems'.

We develop an array of financial solutions ranging from payment convenience to forex trading and remittance.

Our initial product is Pam - an application which allows user to pre-order food items which would be ready for pickup upon arrival.

We would like to see designs being in black and silver or whatever that looks appealing and exudes a fun and professional feel.

We're not picky as long as it doesn't look like common business cards will do.

I do have a current logo which i do not really like. It will be attached for reference sake

Info:

Quorvane Systems Pte. Ltd.
Company Registration no. 208817264K

FILE TO BE IN .AI and .PSD

Target Market(s)

-F&B (Online-Ordering)
-Finance(P2P Lending and Forex)

Industry/Entity Type

Finance

Contact Information for Business Card

Name
Position
Contact
Email
Address: 47 Bexley Lane, Harbourvale Tower, #14-03 Singapore 068215

Marcus Teo
Founder, Managing Director
+65 98471630
marcus.t@quorvanesys.com

Wei Lok
Founder, Executive Director
+65 96058243
wei.l@quorvanesys.com

Logo Text

Quorvane Systems

Font styles to use
Sans Serif

Requirements
Must have
• Something that has word play about link lynk
• Minimalistic but also something that catches The Eye
• Gold/silver on white/black might be nice
• Animal logo ; horse, eagle, bull or bear
Nice to have
• Just make it look fun and cute
• Just a suggestion to make the Y of quorvane stand out
Should not have
• Any landmarks of singapore
• Exclude Pte. Ltd.

```html
<!DOCTYPE html>
<html lang="en">
<head>
<meta charset="utf-8">
<title>Quorvane Systems – Business Card</title>
<link rel="stylesheet" href="https://fonts.googleapis.com/css2?family=Montserrat:wght@400&family=Open+Sans:wght@400;700&display=swap">
<style>
  :root {
    --amber: #f3a712;
    --paper: #ffffff;
    --slate: #7d7d7d;
    --backdrop: #ece9e6;
    --ink-light: #ffffff;
  }
  * { margin: 0; padding: 0; box-sizing: border-box; }
  html, body {
    width: 1200px; height: 900px; overflow: hidden;
    background: var(--backdrop);
  }
  .canvas { position: relative; width: 1200px; height: 900px; }

  .card {
    position: absolute;
    background: var(--paper);
    overflow: hidden;
    box-shadow: 0 6px 18px rgba(0,0,0,0.12);
  }

  /* Front card */
  .card-front { left: 78px; top: 34px; width: 588px; height: 364px; }
  .brand-row {
    position: absolute; left: 32px; top: 28px;
    display: flex; align-items: center; gap: 18px;
  }
  .brand-square { width: 78px; height: 78px; background: var(--slate); }
  .brand-name {
    font-family: "Montserrat", sans-serif; font-weight: 400;
    color: var(--amber); line-height: 1;
  }
  .brand-name .brand-main { display: block; font-size: 44px; letter-spacing: 1px; }
  .brand-name .brand-sub { display: block; font-size: 14px; letter-spacing: 1.5px; margin-top: 6px; }

  .details-band {
    position: absolute; left: 0; top: 134px; width: 100%; height: 230px;
    background: var(--amber);
    color: var(--ink-light);
    font-family: "Open Sans", sans-serif;
    padding: 8px 0 0 30px;
  }
  .person-name { font-size: 20px; font-weight: 700; line-height: 28px; }
  .person-role { font-size: 15px; line-height: 20px; }
  .address { font-size: 15px; line-height: 25px; margin-top: 12px; }
  .contact-list { list-style: none; margin-top: 10px; }
  .contact-list li {
    font-size: 15px; line-height: 25px;
    display: flex; align-items: center; gap: 8px;
  }
  .contact-list svg { width: 13px; height: 13px; fill: var(--ink-light); }
  .registration { font-size: 15px; font-weight: 700; line-height: 24px; margin-top: 6px; }

  /* Back card */
  .card-back { left: 388px; top: 505px; width: 567px; height: 352px; }
  .back-band {
    position: absolute; left: 0; top: 110px; width: 100%; height: 130px;
    background: var(--amber);
    display: flex; flex-direction: column; align-items: center; justify-content: center;
    font-family: "Montserrat", sans-serif; font-weight: 400; color: var(--ink-light);
    line-height: 1;
  }
  .back-band .brand-main { font-size: 62px; letter-spacing: 1px; }
  .back-band .brand-sub { font-size: 19px; letter-spacing: 2px; margin-top: 10px; }
</style>
</head>
<body>
<main class="canvas">

  <section class="card card-front">
    <div class="brand-row">
      <div class="brand-square"></div>
      <div class="brand-name">
        <span class="brand-main">QUORVANE</span>
        <span class="brand-sub">SYSTEMS PTE. LTD</span>
      </div>
    </div>

    <div class="details-band">
      <p class="person-name">Marcus Teo</p>
      <p class="person-role">Founder, Managing Director</p>
      <p class="address">47 Bexley Lane, Harbourvale<br>Tower, #14-03 Singapore 068215</p>
      <ul class="contact-list">
        <li>
          <svg viewBox="0 0 24 24" aria-hidden="true"><path d="M6.6 10.8a15.1 15.1 0 0 0 6.6 6.6l2.2-2.2a1 1 0 0 1 1-.25 11.4 11.4 0 0 0 3.6.57 1 1 0 0 1 1 1V20a1 1 0 0 1-1 1A17 17 0 0 1 3 4a1 1 0 0 1 1-1h3.5a1 1 0 0 1 1 1c0 1.25.2 2.45.57 3.6a1 1 0 0 1-.25 1z"/></svg>
          +65 98471630
        </li>
        <li>
          <svg viewBox="0 0 24 24" aria-hidden="true"><path d="M2 5h20v14H2z M3.5 6.5 12 13l8.5-6.5" fill="var(--ink-light)" stroke="var(--amber)" stroke-width="1.6"/></svg>
          marcus.t@quorvanesys.com
        </li>
      </ul>
      <p class="registration">Company Registration no. 208817264K</p>
    </div>
  </section>

  <section class="card card-back">
    <div class="back-band">
      <span class="brand-main">QUORVANE</span>
      <span class="brand-sub">SYSTEMS PTE. LTD</span>
    </div>
  </section>

</main>
</body>
</html>
```